Marlow's Anvil BBQ Sauce Needs a Label

We are looking for a rustic label that would help our product stand out on a shelf. The company name is Marlow's Anvil. We are a new company looking to stand out on shelving with our amazing BBQ Sweet, Spicy and Rub. The label size needs to be 6.5" wide x 2.5" tall. I have taken a step in creating a label which is attached. This is just an idea for you to bring us an amazing retail ready look. On the left side of the label we need to have a 1 color flag with Made In USA. Also would need to have the address on the same side. Marlow's Anvil BBQ Sauce, Coconut Creek, FL 33073. The nutrition Facts are also needed. The information is correct but would need to be adjusted as to font and sizing. Image 7247 is what I have lightly put together and image 2495 is current logo on actual label. If you need any more guidance please let me know. Dobbs TangBlaze is an example of the pop we would like to see

Requirements
Must have
• Rustic Look
Nice to have
• Rustic look with a feeling similar to image 7247 that’s attached.
Should not have
• Same look as the original logo that’s on the actual label.

```html
<!DOCTYPE html>
<html lang="en">
<head>
<meta charset="utf-8">
<title>Marlow's Anvil BBQ Labels</title>
<link href="https://fonts.googleapis.com/css2?family=Nunito+Sans:wght@400;700;800;900&family=Archivo+Black&family=Lobster&display=swap" rel="stylesheet">
<style>
:root{
  --paper:#efe3c6;
  --paper-edge:#e2c58f;
  --ink:#3a2421;
  --brand-red:#8c1f2c;
  --spicy:#d22a3a;
  --sweet:#2f4ea3;
  --rub:#e0671f;
  --chip:#f6eedb;
  --white:#ffffff;
}
*{margin:0;padding:0;box-sizing:border-box}
html,body{width:1054px;height:1200px;overflow:hidden;background:var(--white)}
body{position:relative;font-family:"Nunito Sans",sans-serif;color:var(--ink)}
.label{
  position:absolute;left:85px;width:882px;height:340px;
  background:radial-gradient(ellipse at 50% 45%,#f4ead2 0%,var(--paper) 55%,var(--paper-edge) 100%);
  overflow:hidden;
}
.label--spicy{top:59px;--accent:var(--spicy)}
.label--sweet{top:429px;--accent:var(--sweet)}
.label--rub{top:798px;--accent:var(--rub)}

.ingredients{position:absolute;left:20px;top:24px;font-size:10px;line-height:12.3px}
.ingredients h3{font-weight:800;font-size:10px}
.storage{position:absolute;left:20px;top:97px;font-size:10px;font-weight:800}
.flag{position:absolute;left:20px;top:207px;width:82px;height:43px}
.origin{position:absolute;left:20px;top:251px;font-size:11.5px;font-weight:900;letter-spacing:.2px}
.maker{position:absolute;left:20px;top:273px;font-size:10px;font-weight:800;line-height:12.3px}
.web{position:absolute;left:20px;top:305px;font-size:10px;font-weight:800}

.band-accent{position:absolute;left:0;right:0;top:327px;height:7px;background:var(--accent)}
.band-dark{position:absolute;left:0;right:0;top:334px;height:6px;background:var(--ink)}

.emblem{
  position:absolute;left:275px;top:30px;width:332px;height:286px;border-radius:40px 40px 166px 166px;
  background:radial-gradient(ellipse at 50% 55%,rgba(140,31,44,.16) 0%,rgba(58,36,33,.12) 55%,rgba(58,36,33,.04) 100%);
}
.recipe{position:absolute;left:0;width:882px;top:34px;text-align:center;font-family:"Lobster",cursive;font-size:17px;color:var(--brand-red)}
.brand-name{
  position:absolute;left:275px;width:332px;top:70px;text-align:center;
  font-family:"Archivo Black",sans-serif;font-weight:400;font-size:40px;line-height:48px;
  color:var(--ink);text-transform:uppercase;letter-spacing:1px
}
.variant{position:absolute;left:390px;top:275px;width:102px;height:29px;background:var(--chip);border-radius:4px;text-align:center;font-family:"Archivo Black",sans-serif;font-size:15px;line-height:29px;color:var(--accent)}
.size{position:absolute;left:545px;top:277px;font-family:"Archivo Black",sans-serif;font-size:17px}

.nutrition{position:absolute;left:707px;top:19px;width:155px;border:1.5px solid var(--ink);padding:3px 7px 5px;font-size:8px;line-height:9.4px}
.nutrition h2{font-family:"Archivo Black",sans-serif;font-size:14.5px;line-height:16px;letter-spacing:.6px;font-weight:400}
.nutrition .row{display:flex;justify-content:space-between;border-bottom:.6px solid var(--ink);padding:1.6px 0}
.nutrition .row.plain{border:0;padding:0}
.nutrition .indent{padding-left:9px}
.nutrition .bar{height:7px;background:var(--ink);margin:2px 0}
.nutrition .bar.thin{height:4px}
.nutrition b{font-weight:800}
.nutrition .small{font-size:6.5px;font-weight:800}
.nutrition .note{font-size:5.4px;line-height:6.2px;margin-top:3px;text-align:justify}
</style>
</head>
<body>

<section class="label label--spicy">
  <div class="ingredients"><h3>Ingredients:</h3>Tomato, Chili Sauce,<br>Vinegar, Worcester,<br>Sugar, Onion, Lemon,<br>Honey and Spices</div>
  <p class="storage">Refrigerate After Opening</p>
  <svg class="flag" viewBox="0 0 82 43" aria-hidden="true"><g fill="var(--ink)"><rect y="0" width="82" height="3"/><rect y="7" width="82" height="3"/><rect y="13" width="82" height="3"/><rect y="20" width="82" height="3"/><rect y="26" width="82" height="3"/><rect y="33" width="82" height="3"/><rect y="40" width="82" height="3"/><rect width="33" height="23"/></g></svg>
  <p class="origin">MADE IN USA</p>
  <p class="maker">Marlow's Anvil BBQ Sauce<br>Coconut Creek, FL 33073</p>
  <p class="web">www.marlowsanvilbbq.com</p>
  <div class="emblem" role="img" aria-label="Rustic brand emblem illustration area"></div>
  <p class="recipe">Original Recipe</p>
  <p class="brand-name">Marlow's<br>Anvil<br>BBQ Sauce</p>
  <p class="variant">SPICY</p>
  <p class="size">16 oz.</p>
  <div class="nutrition">
    <h2>Nutrition Facts</h2>
    <div class="row plain"><span>Serving Size 1 Tbsp. (18g)</span></div>
    <div class="row plain"><span>Servings Per Container</span><span>25</span></div>
    <div class="bar"></div>
    <div class="row small"><span>Amount Per Serving</span></div>
    <div class="row"><span><b>Calories</b> 25</span><span>Calories from Fat 0</span></div>
    <div class="bar thin"></div>
    <div class="row small"><span></span><span>% Daily Value*</span></div>
    <div class="row"><span><b>Total Fat</b> 0g</span><b>0%</b></div>
    <div class="row indent"><span>Saturated Fat 0g</span><b>0%</b></div>
    <div class="row indent"><span>Trans Fat 0g</span></div>
    <div class="row"><span><b>Cholesterol</b> 0mg</span><b>0%</b></div>
    <div class="row"><span><b>Sodium</b> 150mg</span><b>6%</b></div>
    <div class="row"><span><b>Total Carbohydrate</b> 6g</span><b>2%</b></div>
    <div class="row indent"><span>Dietary Fiber 0g</span><b>0%</b></div>
    <div class="row indent"><span>Sugars 6g</span></div>
    <div class="row plain" style="padding:2px 0"><span><b>Protein</b> 0.2g</span></div>
    <div class="bar"></div>
    <div class="row"><span>Vitamin A 1%</span><span>• Vitamin C 1%</span></div>
    <div class="row"><span>Calcium 1%</span><span>• Iron 1%</span></div>
    <p class="note">*Percent Daily Values are based on a 2,000 calorie diet. Your daily values may be higher or lower depending on your calorie needs</p>
  </div>
  <div class="band-accent"></div><div class="band-dark"></div>
</section>

<section class="label label--sweet">
  <div class="ingredients"><h3>Ingredients:</h3>Tomato, Chili Sauce,<br>Vinegar, Worcester,<br>Sugar, Onion, Lemon,<br>Honey and Spices</div>
  <p class="storage">Refrigerate After Opening</p>
  <svg class="flag" viewBox="0 0 82 43" aria-hidden="true"><g fill="var(--ink)"><rect y="0" width="82" height="3"/><rect y="7" width="82" height="3"/><rect y="13" width="82" height="3"/><rect y="20" width="82" height="3"/><rect y="26" width="82" height="3"/><rect y="33" width="82" height="3"/><rect y="40" width="82" height="3"/><rect width="33" height="23"/></g></svg>
  <p class="origin">MADE IN USA</p>
  <p class="maker">Marlow's Anvil BBQ Sauce<br>Coconut Creek, FL 33073</p>
  <p class="web">www.marlowsanvilbbq.com</p>
  <div class="emblem" role="img" aria-label="Rustic brand emblem illustration area"></div>
  <p class="recipe">Original Recipe</p>
  <p class="brand-name">Marlow's<br>Anvil<br>BBQ Sauce</p>
  <p class="variant">SWEET</p>
  <p class="size">16 oz.</p>
  <div class="nutrition">
    <h2>Nutrition Facts</h2>
    <div class="row plain"><span>Serving Size 1 Tbsp. (18g)</span></div>
    <div class="row plain"><span>Servings Per Container</span><span>25</span></div>
    <div class="bar"></div>
    <div class="row small"><span>Amount Per Serving</span></div>
    <div class="row"><span><b>Calories</b> 25</span><span>Calories from Fat 0</span></div>
    <div class="bar thin"></div>
    <div class="row small"><span></span><span>% Daily Value*</span></div>
    <div class="row"><span><b>Total Fat</b> 0g</span><b>0%</b></div>
    <div class="row indent"><span>Saturated Fat 0g</span><b>0%</b></div>
    <div class="row indent"><span>Trans Fat 0g</span></div>
    <div class="row"><span><b>Cholesterol</b> 0mg</span><b>0%</b></div>
    <div class="row"><span><b>Sodium</b> 150mg</span><b>6%</b></div>
    <div class="row"><span><b>Total Carbohydrate</b> 6g</span><b>2%</b></div>
    <div class="row indent"><span>Dietary Fiber 0g</span><b>0%</b></div>
    <div class="row indent"><span>Sugars 6g</span></div>
    <div class="row plain" style="padding:2px 0"><span><b>Protein</b> 0.2g</span></div>
    <div class="bar"></div>
    <div class="row"><span>Vitamin A 1%</span><span>• Vitamin C 1%</span></div>
    <div class="row"><span>Calcium 1%</span><span>• Iron 1%</span></div>
    <p class="note">*Percent Daily Values are based on a 2,000 calorie diet. Your daily values may be higher or lower depending on your calorie needs</p>
  </div>
  <div class="band-accent"></div><div class="band-dark"></div>
</section>

<section class="label label--rub">
  <div class="ingredients"><h3>Ingredients:</h3>Assorted Spices</div>
  <svg class="flag" viewBox="0 0 82 43" aria-hidden="true"><g fill="var(--ink)"><rect y="0" width="82" height="3"/><rect y="7" width="82" height="3"/><rect y="13" width="82" height="3"/><rect y="20" width="82" height="3"/><rect y="26" width="82" height="3"/><rect y="33" width="82" height="3"/><rect y="40" width="82" height="3"/><rect width="33" height="23"/></g></svg>
  <p class="origin">MADE IN USA</p>
  <p class="maker">Marlow's Anvil BBQ Sauce<br>Coconut Creek, FL 33073</p>
  <p class="web">www.marlowsanvilbbq.com</p>
  <div class="emblem" role="img" aria-label="Rustic brand emblem illustration area"></div>
  <p class="recipe">Original Recipe</p>
  <p class="brand-name">Marlow's<br>Anvil<br>BBQ Sauce</p>
  <p class="variant">RUB</p>
  <p class="size">8 Oz.</p>
  <div class="nutrition">
    <h2>Nutrition Facts</h2>
    <div class="row plain"><span>Serving Size 1 Tsp. (5g)</span></div>
    <div class="row plain"><span>Servings Per Container</span><span>45</span></div>
    <div class="bar"></div>
    <div class="row small"><span>Amount Per Serving</span></div>
    <div class="row"><span><b>Calories</b> 0</span></div>
    <div class="bar thin"></div>
    <div class="row small"><span></span><span>% Daily Value*</span></div>
    <div class="row"><span><b>Total Fat</b> 0g</span><b>0%</b></div>
    <div class="row"><span><b>Sodium</b> 70mg</span><b>3%</b></div>
    <div class="row"><span><b>Total Carbohydrate</b> 0mg</span><b>0%</b></div>
    <div class="row plain" style="padding:2px 0"><span><b>Protein</b> 0g</span></div>
    <div class="bar"></div>
    <p class="note">Not a significant source of calories from fat, saturated fat, trans fat, cholesterol, dietary fiber, sugars, vitamin A, vitamin C, calcium, iron.</p>
    <p class="note">*Percent Daily Values are based on a 2,000 calorie diet.</p>
  </div>
  <div class="band-accent"></div><div class="band-dark"></div>
</section>

</body>
</html>
```